landscaping core flute signs

I need core flutes created with business name and a few extra dot points for putting on fences for job sites 120cm x 120cm approx.
I want our old ones information with the new L logo and colour palette

```html
<!DOCTYPE html>
<html lang="en">
<head>
<meta charset="utf-8">
<title>Grounded Form – Job Site Sign</title>
<link rel="stylesheet" href="https://fonts.googleapis.com/css2?family=Cinzel:wght@500&family=Arimo:wght@400;700&display=swap">
<style>
  :root {
    --backdrop: #9a9a9a;
    --sign-black: #131313;
    --leaf-green: #5e8f57;
    --white: #ffffff;
  }
  * { margin: 0; padding: 0; box-sizing: border-box; }
  html, body { width: 1200px; height: 829px; overflow: hidden; background: var(--backdrop); }
  .sign {
    position: absolute; left: 281px; top: 96px;
    width: 637px; height: 637px;
    background: var(--sign-black);
    color: var(--white);
    font-family: "Arimo", Arial, sans-serif;
    overflow: hidden;
  }
  .brand-mark {
    position: absolute; left: 238px; top: 28px;
    width: 160px; height: 160px; border-radius: 50%;
    background: var(--leaf-green);
  }
  .brand-name {
    position: absolute; left: 0; right: 0; top: 204px;
    text-align: center;
    font-family: "Cinzel", "Times New Roman", serif;
    font-weight: 500; font-size: 48px; line-height: 1;
    letter-spacing: 1px;
  }
  .brand-sub {
    position: absolute; left: 0; right: 0; top: 252px;
    display: flex; align-items: center; justify-content: center; gap: 18px;
    font-family: "Cinzel", "Times New Roman", serif;
    font-weight: 500; font-size: 26px; line-height: 1; letter-spacing: 7px;
  }
  .brand-sub::before, .brand-sub::after {
    content: ""; width: 76px; height: 2px; background: var(--white);
  }
  .tagline {
    position: absolute; left: 0; right: 0; top: 283px;
    text-align: center;
    font-family: "Cinzel", "Times New Roman", serif;
    font-size: 13px; letter-spacing: 4px; color: var(--leaf-green);
  }
  .services { position: absolute; left: 181px; top: 333px; list-style: none; }
  .services li {
    display: flex; align-items: center; gap: 14px;
    height: 49px; font-size: 25px; color: var(--leaf-green);
  }
  .services li::before {
    content: ""; width: 22px; height: 22px; border-radius: 50%;
    background: var(--leaf-green); flex: none;
  }
  .phone {
    position: absolute; left: 0; right: 0; top: 472px;
    text-align: center; font-weight: 700; font-size: 62px; line-height: 1;
  }
  .email {
    position: absolute; left: 0; right: 0; top: 548px;
    text-align: center; font-weight: 700; font-size: 28px; line-height: 1;
  }
  .licence-band { position: absolute; left: 0; top: 598px; width: 637px; height: 39px; }
  .licence {
    position: absolute; left: 218px; width: 203px; top: 604px;
    text-align: center; font-weight: 700; font-size: 19px; letter-spacing: 0.5px;
  }
</style>
</head>
<body>
  <main class="sign">
    <div class="brand-mark" aria-hidden="true"></div>
    <h1 class="brand-name">GROUNDED</h1>
    <div class="brand-sub">FORM</div>
    <p class="tagline">STRUCTURAL LANDSCAPING</p>

    <ul class="services">
      <li>Paving &amp; Concreting</li>
      <li>Fencing &amp; Retaining</li>
      <li>Desgin &amp; Construct</li>
    </ul>

    <p class="phone">0400 123 987</p>
    <p class="email">sam@groundedform.com</p>

    <svg class="licence-band" viewBox="0 0 637 39" aria-hidden="true">
      <rect x="0" y="11" width="637" height="3" fill="var(--white)"/>
      <path d="M232 4 H407 Q414 4 417 10 L428 39 H210 L221 10 Q224 4 232 4 Z" fill="var(--leaf-green)"/>
    </svg>
    <p class="licence">QBSA:&nbsp; 1234567</p>
  </main>
</body>
</html>
```